Create a Magazine Ad for an asbestos law firm

we need an 8 X 13 ad to be on the back of a magazine cover. We have the text Attached and want a similar look and feel to our website : www.harborvale-claims.example. The ad should be targeted to white males 55 years or older who are conservative and worked in industry or industrial plants. The main offer is a free case review and trying to get them to call the telephone number.

Target Market(s)

White collar men who worked in industrial plants. Age 55 years or older.

Industry/Entity Type

Legal

Requirements
Must have
• Pictures of white middle class conservative man or man and woman
Nice to have
• look at www.harborvale-claims.example to an. idea of what we are looking for

```html
<!DOCTYPE html>
<html lang="en">
<head>
<meta charset="utf-8">
<title>Harborvale Claims – Mesothelioma Compensation Ad</title>
<link href="https://fonts.googleapis.com/css2?family=Questrial&family=Figtree:wght@600;700&display=swap" rel="stylesheet">
<style>
  :root{
    --sky:#6591a8;
    --deep:#216889;
    --mid:#4f849f;
    --yellow:#fdfd66;
    --white:#ffffff;
    --soft:#e8f0f4;
    --ink:#0b0b0b;
    --brand-ink:#2f5f72;
  }
  *{margin:0;padding:0;box-sizing:border-box}
  html,body{width:738px;height:1200px;overflow:hidden}
  body{font-family:"Questrial",sans-serif;color:var(--soft);background:var(--sky)}
  .ad{position:relative;width:738px;height:1200px;overflow:hidden;
      background:linear-gradient(180deg,var(--sky) 0,var(--sky) 746px,var(--mid) 780px,var(--deep) 1140px)}
  .abs{position:absolute}

  .headline{left:47px;top:46px;color:var(--white);text-transform:uppercase;line-height:1}
  .headline .lead{display:block;font-size:19.5px;letter-spacing:.2px}
  .headline .big{display:block;font-size:45px;margin-top:6px;letter-spacing:.5px}
  .headline .mark{display:inline-block;margin-top:6px;background:var(--yellow);color:var(--ink);
      font-size:27px;padding:3px 4px 2px 4px;width:322px;letter-spacing:.3px}

  .brand{left:390px;top:48px;width:348px;height:97px;background:var(--white);
      display:flex;flex-direction:column;justify-content:center;padding-left:30px;color:var(--brand-ink)}
  .brand .name{display:flex;align-items:center;gap:10px;font-size:27px}
  .brand .dot{width:18px;height:18px;border-radius:50%;background:var(--brand-ink)}
  .brand .tag{font-size:11px;margin-top:5px}

  .photo-band{left:0;top:318px;width:738px;height:428px;
      background:linear-gradient(120deg,#6f96ab 0%,#5f8aa1 40%,#7a9fb3 70%,#6b93a9 100%)}

  .intro{left:50px;top:172px;width:640px;font-size:17px;line-height:22px}
  .list{list-style:none;font-size:16px}
  .list li{position:relative;padding-left:18px;height:24.4px;line-height:22px}
  .list li::before{content:"";position:absolute;left:0;top:7px;width:8px;height:8px;border-radius:50%;background:var(--yellow)}
  .list-a{left:50px;top:230px}
  .list-b{left:50px;top:357px}

  .qualify{left:0;top:319px;width:474px;height:28px;background:var(--yellow);color:var(--ink);
      font-size:16px;line-height:28px;padding-left:44px}

  .portraits{left:527px;top:261px;width:165px;height:301px;border-radius:83px;background:var(--yellow)}
  .portrait{position:absolute;left:15px;width:135px;height:135px;border-radius:50%}
  .portrait.one{top:15px;background:linear-gradient(135deg,#c9c2b6,#e8e2d8 55%,#9aa4a8)}
  .portrait.two{top:154px;background:linear-gradient(160deg,#3e4448,#a9a39c 50%,#2f3338)}

  .h2{font-family:"Figtree",sans-serif;font-weight:700;color:var(--yellow);font-size:20.5px;line-height:31px}
  .trust-title{left:50px;top:602px}
  .trust-text{left:50px;top:633px;width:645px;font-size:17px;line-height:22.3px}
  .money-title{left:50px;top:723px;width:610px}
  .money-text{left:50px;top:785px;width:655px;font-size:17px;line-height:22.3px}

  .results{left:50px;top:882px;width:652px;height:165px;border:1.2px solid var(--yellow);border-radius:18px}
  .result{position:absolute;font-size:14.6px;line-height:19px;color:var(--white)}
  .c1{left:34px}.c2{left:368px}
  .r1{top:11px}.r2{top:66px}.r3{top:121px}

  .cta{left:44px;top:1058px;width:650px;text-align:center;font-family:"Figtree",sans-serif;font-weight:600;
      font-size:15.5px;line-height:23.5px;color:var(--white)}
  .cta em{font-style:normal;color:var(--yellow)}
  .call{left:0;top:1107px;width:738px;text-align:center;font-family:"Figtree",sans-serif;font-weight:600;
      font-size:21.5px;color:var(--white)}

  .footer{left:0;top:1140px;width:738px;height:60px;background:var(--yellow);color:var(--ink);
      text-align:center;font-size:16.8px;padding-top:9px}
</style>
</head>
<body>
<div class="ad">
  <div class="abs photo-band" role="img" aria-label="Photo of a smiling older man with glasses embraced by his wife"></div>

  <h1 class="abs headline">
    <span class="lead">Diagnosed with Mesothelioma,</span>
    <span class="big">You could be</span>
    <span class="mark">Owed Compensation</span>
  </h1>

  <div class="abs brand">
    <div class="name"><span class="dot"></span>Harborvale Claims</div>
    <div class="tag">Standing with patients and families since 2003</div>
  </div>

  <p class="abs intro">It's very likely you developed this disease through asbestos exposure. Mesothelioma patients are getting multi-million dollar settlements, decades later, from:</p>
  <ul class="abs list list-a">
    <li>Exposure to asbestos products,</li>
    <li>Ex-employers, or</li>
    <li>Talcum baby powder companies.</li>
  </ul>

  <div class="abs qualify">We can help you find out if you qualify for a case in minutes.</div>

  <ul class="abs list list-b">
    <li>We'll analyze your situation at no cost</li>
    <li>Determine how much compensation you could be entitled too</li>
    <li>Show you the next steps to get what you're owed</li>
  </ul>

  <div class="abs portraits">
    <div class="portrait one" role="img" aria-label="Photo of a doctor consulting with a smiling senior man"></div>
    <div class="portrait two" role="img" aria-label="Photo of an elderly veteran wearing a service cap"></div>
  </div>

  <h2 class="abs h2 trust-title">$30 Billion is Available in Trust for Mesothelioma Patients</h2>
  <p class="abs trust-text">Tradesmen in many industries were negligently exposed to asbestos materials well into the 1990s. Whether you developed Mesothelioma yourself due to asbestos exposure or you're the surviving family of a lost loved one you could be entitled to significant compensation.</p>

  <h2 class="abs h2 money-title">How much Money Can People Receive from a Mesothelioma Case?</h2>
  <p class="abs money-text">Depending on where you were exposed and a few other factors, you can get a settlement from 6 to 7 figures. Here are a few examples of Mesothelioma Settlements received by our clients. These figures are the total compensation after all attorney fees and expenses are deducted.</p>

  <div class="abs results">
    <div class="result c1 r1">$6,142,500<br>Exposed through heavy duty vehicles</div>
    <div class="result c1 r2">$6,033,510<br>Exposed through general contracting</div>
    <div class="result c1 r3">$5,939,010<br>Exposed through boat repair</div>
    <div class="result c2 r1">$3,921,750<br>Exposed through navy service</div>
    <div class="result c2 r2">$3,600,450<br>Exposed through navy service</div>
    <div class="result c2 r3">$2.5 Million<br>Exposed from Talcum Baby Powder.</div>
  </div>

  <p class="abs cta"><em>Find out if you're Eligible, for FREE, in Minutes.</em> We'll evaluate your situation and tell you what your case could be worth. <em>Get your Free evaluation now!</em></p>
  <p class="abs call">CALL 1-XXX XXXX (good number)</p>

  <div class="abs footer">Brightwell &amp; Osgood, LLP, Martin Brightwell, Houston, TX</div>
</div>
</body>
</html>
```